International Trading Company, 'KIRO' needs a Business Card

The company name is "KIRO" and it has own logo design.
I'd like to use its logo on this business card.
I need two side Business Card.
I'll look forward to your great design.
Thank you very much in advance.

Contact Information for Business Card

Company Name : Kiro Harbour Limited
Information Example
Dorian Pallister
Mobile(use icon please) : 1 (212) 555-0143
Tel(use icon please) : 1 (212) 555-0178
Email(use icon please) : dorian27@kiroharbour-mail.com
Address(use icon please) : 482 Halden Ave, New York, NY 10160, USA

```html
<!DOCTYPE html>
<html lang="en">
<head>
<meta charset="utf-8">
<title>Kiro Harbour Limited – Business Card</title>
<link rel="stylesheet" href="https://fonts.googleapis.com/css2?family=Open+Sans:wght@700;800&family=Noto+Serif:wght@400;700&display=swap">
<style>
  :root {
    --stage: #3b3140;
    --photo-light: #e4e4e4;
    --photo-mid: #bdbdbd;
    --photo-dark: #8f8f8f;
    --band: rgba(255, 255, 255, 0.72);
    --ink-grey: #3f3f42;
    --ink-navy: #14182b;
    --ink-body: #2a2a2e;
  }
  * { box-sizing: border-box; margin: 0; padding: 0; }
  html, body { width: 1200px; height: 800px; overflow: hidden; }
  body {
    background: var(--stage);
    display: flex;
    align-items: center;
    justify-content: center;
    gap: 40px;
  }
  .card {
    position: relative;
    width: 550px;
    height: 314px;
    overflow: hidden;
    border-radius: 3px;
    box-shadow: 0 10px 30px rgba(0, 0, 0, 0.35);
  }
  .card__photo {
    position: absolute;
    inset: 0;
    background:
      linear-gradient(180deg,
        var(--photo-dark) 0%,
        var(--photo-mid) 18%,
        var(--photo-light) 40%,
        var(--photo-light) 62%,
        var(--photo-mid) 80%,
        var(--photo-dark) 100%);
  }
  .card__band {
    position: absolute;
    left: 0;
    right: 0;
    top: 22%;
    height: 52%;
    background: var(--band);
  }
  .card__back-band { top: 18%; height: 46%; }

  /* Front */
  .front__logo {
    position: absolute;
    left: 0;
    right: 0;
    top: 50%;
    transform: translateY(-55%);
    text-align: center;
    font-family: "Open Sans", sans-serif;
    font-weight: 800;
    font-size: 104px;
    letter-spacing: 2px;
    color: var(--ink-grey);
  }

  /* Back */
  .back__company {
    position: absolute;
    left: 44px;
    top: 62px;
    font-family: "Open Sans", sans-serif;
    font-weight: 800;
    font-size: 27px;
    letter-spacing: -0.5px;
    text-transform: uppercase;
    color: var(--ink-grey);
  }
  .back__logo {
    position: absolute;
    left: 44px;
    top: 104px;
    font-family: "Open Sans", sans-serif;
    font-weight: 800;
    font-size: 46px;
    color: var(--ink-grey);
  }
  .back__person {
    position: absolute;
    left: 262px;
    top: 168px;
  }
  .back__name {
    font-family: "Noto Serif", serif;
    font-weight: 700;
    font-size: 20px;
    color: var(--ink-navy);
    margin-bottom: 4px;
  }
  .back__details {
    list-style: none;
    font-family: "Noto Serif", serif;
    font-size: 11px;
    line-height: 1.4;
    color: var(--ink-body);
  }
  .back__label { font-weight: 700; }
</style>
</head>
<body>
  <section class="card card--front" aria-label="Card front">
    <div class="card__photo" role="img" aria-label="Greyscale photograph of a harbour-side building"></div>
    <div class="card__band"></div>
    <div class="front__logo">KIRO</div>
  </section>

  <section class="card card--back" aria-label="Card back">
    <div class="card__photo" role="img" aria-label="Greyscale photograph of a harbour-side building"></div>
    <div class="card__band card__back-band"></div>
    <h1 class="back__company">Kiro Harbour Limited</h1>
    <div class="back__logo">KIRO</div>
    <div class="back__person">
      <h2 class="back__name">Dorian Pallister</h2>
      <ul class="back__details">
        <li>482 Halden Ave, New York,</li>
        <li>NY 10160, USA</li>
        <li><span class="back__label">tel:</span> 1 (212) 555-0178</li>
        <li><span class="back__label">mobil:</span> 1 (212) 555-0143</li>
        <li><span class="back__label">email:</span> dorian27@kiroharbour-mail.com</li>
      </ul>
    </div>
  </section>
</body>
</html>
```